Vintage pharmacy themed coffee bag label

This is a coffee label for the signature blend of a medical apothecary (vintage pharmacy) themed coffee company that donates proceeds to fund medical care around the world.

I want the design to scream old/vintage pharmacy such as examples attached (example-asthmacig, citratemagnesia, french-label, witch-sample ). I'd like the label to roughly mimic the setup of the example-asthmacig but with a bit more intricate lettering and design like the other examples have.

Target Market(s)

Higher end coffee drinkers

Industry/Entity Type

It Company

Font styles to use
Serif
Decorative
Script

Colors
191919
7f7f7f
e0e0e0

Requirements
Must have
• The actual text with basic outline is attached as "Actual text for label." I'd like the photo to be of the doctor attached (Dr Kessler). I also attached the png of the logo to be included on the label with the website right below it
Nice to have
• Colors should be similar to the attached examples. But mostly black/dark brown font with the off white/brown background
Should not have
• nothing that comes to mind

```html
<!DOCTYPE html>
<html lang="en">
<head>
<meta charset="utf-8">
<title>Dr. Kessler's Quorva – Coffee Label</title>
<link rel="stylesheet" href="https://fonts.googleapis.com/css2?family=Arvo:wght@700&family=Rye&family=Work+Sans:wght@500;600;700&family=Oswald:wght@300&family=PT+Serif&display=swap">
<style>
  :root {
    --page-bg: #2b2b2b;
    --paper: #efe8d8;
    --paper-edge: #e2d6bd;
    --ink: #191919;
    --ink-soft: #2a2624;
    --apothecary-red: #962427;
    --portrait-light: #bdb8b0;
    --portrait-dark: #3c3a38;
    --band-text: #f3eee4;
  }
  * { box-sizing: border-box; margin: 0; padding: 0; }
  html, body { width: 1200px; height: 900px; overflow: hidden; }
  body { background: var(--page-bg); position: relative; }

  .label {
    position: absolute;
    left: 312px; top: 50px;
    width: 576px; height: 800px;
    background: radial-gradient(ellipse at 50% 45%, var(--paper) 55%, var(--paper-edge) 100%);
    color: var(--ink);
  }
  .label__frame {
    position: absolute; inset: 17px;
    border: 2px solid var(--ink);
    border-radius: 10px;
  }
  .label__frame::after {
    content: ""; position: absolute; inset: 6px;
    border: 1px solid var(--ink);
    border-radius: 6px;
  }

  .maker-arc { position: absolute; left: 148px; top: 52px; width: 280px; height: 120px; }
  .maker-arc text { font-family: "Arvo", serif; font-weight: 700; font-size: 26px; fill: var(--ink); letter-spacing: 0.5px; }

  .portrait {
    position: absolute; left: 222px; top: 115px;
    width: 132px; height: 120px; border-radius: 66px 66px 60px 60px;
    background: radial-gradient(circle at 50% 35%, var(--portrait-light) 0%, #8d8882 45%, var(--portrait-dark) 100%);
  }

  .product-name { position: absolute; left: 60px; top: 232px; width: 456px; height: 150px; }
  .product-name text { font-family: "Rye", serif; font-size: 122px; }
  .product-name .shadow { fill: var(--ink); }
  .product-name .face { fill: var(--apothecary-red); }

  .claim-band {
    position: absolute; left: 61px; top: 395px;
    width: 455px; height: 56px;
    background: var(--ink);
    border-radius: 4px;
    color: var(--band-text);
    font-family: "Work Sans", sans-serif; font-weight: 600;
    font-size: 18px; line-height: 23px; letter-spacing: 0.4px;
    text-align: center;
    display: flex; flex-direction: column; justify-content: center;
  }

  .info { position: absolute; top: 472px; font-family: "PT Serif", serif; font-size: 14.5px; line-height: 20px; color: var(--ink-soft); letter-spacing: -0.3px; }
  .info__heading {
    font-family: "Oswald", sans-serif; font-weight: 300;
    color: var(--apothecary-red);
    font-size: 29px; line-height: 30px; letter-spacing: 0.2px;
    margin-bottom: 6px;
  }
  .info--ingredients { left: 87px; width: 150px; }
  .info--directions { left: 270px; width: 240px; }

  .column-rule { position: absolute; left: 250px; top: 472px; width: 2px; height: 148px; background: var(--ink); }
  .column-rule::after {
    content: ""; position: absolute; left: -3px; top: 66px;
    width: 8px; height: 8px; background: var(--paper);
    border: 1.5px solid var(--ink); transform: rotate(45deg);
  }

  .dosage {
    position: absolute; left: 61px; top: 632px; width: 455px; height: 37px;
    border-top: 1.5px solid var(--ink); border-bottom: 1.5px solid var(--ink);
    color: var(--apothecary-red);
    font-family: "Work Sans", sans-serif; font-weight: 700;
    font-size: 20px; letter-spacing: 0.6px;
    display: flex; align-items: center; justify-content: center;
  }

  .footer-text {
    position: absolute; font-family: "Oswald", sans-serif; font-weight: 300;
    font-size: 17px; line-height: 20px; color: var(--ink-soft);
  }
  .footer-text--site { left: 61px; top: 710px; }
  .footer-text--weight { left: 464px; top: 700px; }

  .brand-mark {
    position: absolute; left: 201px; top: 690px; width: 170px; height: 68px;
    display: flex; align-items: center; justify-content: center; gap: 8px;
    font-family: "Work Sans", sans-serif; font-weight: 600;
    font-size: 19px; letter-spacing: 1.5px; color: var(--ink);
  }
  .brand-mark__dot { width: 10px; height: 10px; border-radius: 50%; background: var(--ink); }
</style>
</head>
<body>
  <main class="label">
    <div class="label__frame"></div>

    <svg class="maker-arc" viewBox="0 0 280 120" aria-label="Dr. Kessler's">
      <defs><path id="maker-curve" d="M12,112 A128,100 0 0 1 268,112"/></defs>
      <text><textPath href="#maker-curve" startOffset="50%" text-anchor="middle">DR.KESSLER'S</textPath></text>
    </svg>

    <div class="portrait" role="img" aria-label="Black and white portrait of Dr. Kessler"></div>

    <svg class="product-name" viewBox="0 0 456 150" aria-label="Quorva">
      <text class="shadow" x="232" y="138" text-anchor="middle" textLength="440" lengthAdjust="spacingAndGlyphs">QUORVA</text>
      <text class="face" x="228" y="134" text-anchor="middle" textLength="440" lengthAdjust="spacingAndGlyphs">QUORVA</text>
    </svg>

    <div class="claim-band">
      <span>FOR THE TEMPORARY RELIEF OF</span>
      <span>PAROXYSMS OF FATIGUE &amp; EXHAUSTION</span>
    </div>

    <section class="info info--ingredients">
      <h2 class="info__heading">ACTIVE INGREDIENTS</h2>
      <p>Iron skillet roasted Ethiopian Yirgacheffe coffee, caffeine.</p>
    </section>

    <div class="column-rule"></div>

    <section class="info info--directions">
      <h2 class="info__heading">DIRECTIONS</h2>
      <p>For pour over variety, mix one part coffee to 10 parts water (i.e. 20 g coffee to 200 g water). Coffee grounds to approximate table salt and not to exceed in size the head of a pin.</p>
    </section>

    <div class="dosage">REPEAT EVERY 4 TO 6 HOURS AS NEEDED</div>

    <p class="footer-text footer-text--site">ALVOCOFFEE.COM</p>
    <div class="brand-mark"><span class="brand-mark__dot"></span><span>ALVO COFFEE</span></div>
    <p class="footer-text footer-text--weight">NET WT<br>12 OZ</p>
  </main>
</body>
</html>
```